Package design for Terrarium Kit

We are putting together a kit to allow people to put build their own terrarium. Our company 'Brightwell Goods' is using the items in a kit supplied by Fern Hollow and adding a 700ml glass jar with a cork lid and rebranding it. We will be using a similar box to the existing Fern Hollow kit and we are asking you to design a new 'wrap' for it with our logo and suggestions about a name for the product. The kit will be Locally Crafted.
Updates

Reason: We realise that to get the quality of design that we are after that you would require more time.

Target Market(s)

People wanting something on their desks, a gift for someone. We will sell it to nurseries, gift shops etc.

Industry/Entity Type

It Company

Requirements
Must have
• Front and back designs.
Nice to have
• Looking for a simple design that is self explanatory but is eye-catching.

```html
<!DOCTYPE html>
<html lang="en">
<head>
<meta charset="utf-8">
<title>Moss Nook – Box Wrap</title>
<link href="https://fonts.googleapis.com/css2?family=Great+Vibes&family=Yellowtail&family=Oswald:wght@400&family=Open+Sans:wght@400&display=swap" rel="stylesheet">
<style>
  :root {
    --stage: #e9ebee;
    --panel-teal: #7fc9bd;
    --panel-teal-light: #a6ddd2;
    --panel-teal-deep: #5fb3ad;
    --foliage-cream: #e8e4c8;
    --foliage-blue: #3f7fc4;
    --foliage-green: #3fae9a;
    --band-blue: rgba(90, 190, 220, 0.55);
    --ink: #121414;
    --accent-yellow: #e8e838;
    --jar-glass: #cfd6d4;
    --jar-moss: #5d9a3a;
    --jar-soil: #2a2620;
  }
  * { box-sizing: border-box; margin: 0; padding: 0; }
  html, body {
    width: 1200px; height: 1006px; overflow: hidden;
    background: var(--stage);
  }
  .wrap {
    position: absolute; left: 135px; top: 50px;
    width: 930px; height: 906px;
    display: flex;
    box-shadow: 0 18px 30px rgba(0,0,0,0.18);
  }
  .foliage-strip {
    width: 90px; height: 100%;
    background: linear-gradient(180deg, var(--foliage-green) 0%, var(--foliage-cream) 18%, var(--foliage-blue) 40%, var(--foliage-green) 60%, var(--foliage-cream) 78%, var(--foliage-green) 100%);
  }
  .face {
    position: relative;
    width: 330px; height: 100%;
    background: linear-gradient(180deg, var(--panel-teal-light) 0%, var(--panel-teal) 45%, var(--panel-teal-deep) 100%);
    text-align: center;
    color: var(--ink);
  }
  .band {
    position: absolute; left: 0; right: 0; height: 6px;
    background: var(--band-blue);
  }
  .band.upper { top: 222px; }
  .band.lower { top: 700px; }
  .maker-name {
    position: absolute; top: 92px; left: 0; right: 0;
    font-family: "Great Vibes", cursive;
    font-size: 52px; line-height: 1;
    white-space: nowrap;
  }
  .brand {
    position: absolute; top: 178px; left: 0; right: 0;
    display: flex; justify-content: center; align-items: center; gap: 10px;
    font-family: "Oswald", sans-serif; font-size: 22px;
    white-space: nowrap;
  }
  .brand-dot {
    width: 34px; height: 34px; border-radius: 50%;
    background: var(--accent-yellow);
  }
  .product-name {
    position: absolute; top: 240px; left: 0; right: 0;
    font-family: "Yellowtail", cursive;
    font-size: 54px; line-height: 1;
    white-space: nowrap;
  }
  .jar-photo {
    position: absolute; top: 332px; left: 58px;
    width: 214px; height: 508px;
    border-radius: 40px 40px 30px 30px;
    background: linear-gradient(180deg, var(--jar-glass) 0%, #dfe5e2 35%, #9fc77a 55%, var(--jar-moss) 72%, var(--jar-soil) 88%, #6d5f4c 100%);
  }
  .volume {
    position: absolute; bottom: 22px; left: 0; right: 0;
    font-family: "Open Sans", sans-serif; font-size: 17px;
  }
</style>
</head>
<body>
  <div class="wrap">
    <div class="foliage-strip" role="img" aria-label="Decorative tropical leaf pattern in teal, blue and cream"></div>

    <section class="face">
      <div class="band upper"></div>
      <div class="band lower"></div>
      <div class="maker-name">Fern Hollow</div>
      <div class="brand"><span class="brand-dot"></span><span>Brightwell Goods</span></div>
      <div class="product-name">moss nook</div>
      <div class="jar-photo" role="img" aria-label="Photograph of a glass jar terrarium with ferns, moss, stones and soil"></div>
      <div class="volume">700ml</div>
    </section>

    <div class="foliage-strip" role="img" aria-label="Decorative tropical leaf pattern in teal, blue and cream"></div>

    <section class="face">
      <div class="band upper"></div>
      <div class="band lower"></div>
      <div class="maker-name">Fern Hollow</div>
      <div class="brand"><span class="brand-dot"></span><span>Brightwell Goods</span></div>
      <div class="product-name">moss nook</div>
      <div class="jar-photo" role="img" aria-label="Photograph of a glass jar terrarium with ferns, moss, stones and soil"></div>
      <div class="volume">700ml</div>
    </section>

    <div class="foliage-strip" role="img" aria-label="Decorative tropical leaf pattern in teal, blue and cream"></div>
  </div>
</body>
</html>
```